Author/ Speaker Business Card design

I need a business card designed that will go with the branding that is already on my book and website. I like clean and straightforward, but I am not opposed to something more 'innovative'.

Target Market(s)

Colleges and Universities, educational institutions

Industry/Entity Type

Education

Contact Information for Business Card

Standard size. It should be able to be printed on good quality white or ivory paper.

Font styles to use
Sans Serif

Colors
0355a3

Requirements
Must have
• There's a blue on my website. It should have some blue. My logo is at the top. It should have the logo incorporated somewhere on it. My name, Author | Speaker | Teacher | Trainer, my phone number (+31 64-207 5184), my email address (milo@thebrightlearner.example), Social media icons (twitter, Instagram, LinkedIn) with the addresses (twitter @writermilohart, Instagram - thebrightlearner, LinkedIn - thebrightlearner) By they way, the website is www.thebrightlearner.example. There is a photo of the book on the website. Also, my full name is Milo Hart
Nice to have
• Try to use the font that is on the website and book. Also, if you could get that blue, that would be great.
Should not have
• My photo

```html
<!DOCTYPE html>
<html lang="en">
<head>
<meta charset="utf-8">
<title>The Bright Learner – Business Card</title>
<link href="https://fonts.googleapis.com/css2?family=Roboto:wght@300;400;500;700&display=swap" rel="stylesheet">
<style>
  :root {
    --brand-blue: #0f55a5;
    --ink-grey: #4a4a4a;
    --paper: #f3f3f1;
    --backdrop: #dcdcdc;
  }
  * { margin: 0; padding: 0; box-sizing: border-box; }
  html, body { width: 1200px; height: 900px; overflow: hidden; }
  body {
    background: var(--backdrop);
    font-family: "Roboto", Arial, sans-serif;
    position: relative;
  }
  .card {
    position: absolute;
    top: 135px;
    width: 361px;
    height: 631px;
  }
  .card--front { left: 185px; background: var(--paper); color: var(--ink-grey); }
  .card--back  { left: 655px; background: var(--brand-blue); }

  .brand {
    position: absolute;
    left: 0; right: 0;
    display: flex;
    align-items: center;
    justify-content: center;
    gap: 12px;
    font-weight: 500;
    line-height: 1;
  }
  .brand__dot { width: 26px; height: 26px; border-radius: 50%; flex: none; }
  .brand__name { font-size: 30px; letter-spacing: -0.3px; }
  .card--front .brand { top: 102px; color: var(--brand-blue); }
  .card--front .brand__dot { background: var(--brand-blue); }
  .card--back .brand { top: 295px; color: #fff; }
  .card--back .brand__dot { background: #fff; }

  .person { position: absolute; top: 262px; left: 0; right: 0; text-align: center; }
  .person__name {
    color: var(--brand-blue);
    font-weight: 500;
    font-size: 30px;
    letter-spacing: 0.5px;
    line-height: 1;
  }
  .person__roles { margin-top: 10px; font-weight: 300; font-size: 15.5px; line-height: 1; }
  .person__rule {
    width: 249px; height: 1.5px; margin: 10px auto 0;
    background: var(--brand-blue);
  }

  .icon-row {
    position: absolute; left: 0; right: 0;
    display: flex; justify-content: center; gap: 9px;
  }
  .icon-row--social { top: 382px; }
  .icon-row--contact { top: 481px; gap: 6px; }
  .social-dot { width: 12px; height: 12px; border-radius: 50%; background: var(--brand-blue); }

  .lines {
    position: absolute; left: 0; right: 0;
    text-align: center; font-weight: 300; font-size: 16px; line-height: 19.5px;
  }
  .lines--social { top: 407px; }
  .lines--contact { top: 505px; }
  .web-domain { color: var(--brand-blue); font-weight: 500; }
</style>
</head>
<body>

  <section class="card card--front">
    <div class="brand">
      <span class="brand__dot"></span>
      <span class="brand__name">The Bright Learner</span>
    </div>

    <div class="person">
      <h1 class="person__name">MILO HART</h1>
      <p class="person__roles">Author | Speaker | Teacher | Trainer</p>
      <div class="person__rule"></div>
    </div>

    <div class="icon-row icon-row--social">
      <span class="social-dot"></span>
      <span class="social-dot"></span>
      <span class="social-dot"></span>
    </div>
    <div class="lines lines--social">
      <p>@writermilohart</p>
      <p>thebrightlearner</p>
      <p>thebrightlearner</p>
    </div>

    <div class="icon-row icon-row--contact">
      <svg width="11" height="11" viewBox="0 0 24 24" aria-label="Phone"><path fill="#0f55a5" d="M6.6 10.8a15 15 0 0 0 6.6 6.6l2.2-2.2c.3-.3.7-.4 1-.2 1.1.4 2.3.6 3.6.6.6 0 1 .4 1 1V20c0 .6-.4 1-1 1A17 17 0 0 1 3 4c0-.6.4-1 1-1h3.5c.6 0 1 .4 1 1 0 1.3.2 2.5.6 3.6.1.3 0 .7-.2 1z"/></svg>
      <svg width="13" height="11" viewBox="0 0 26 20" aria-label="Email"><rect x="1.5" y="1.5" width="23" height="17" fill="none" stroke="#0f55a5" stroke-width="2.5"/><path d="M2 3l11 8 11-8" fill="none" stroke="#0f55a5" stroke-width="2.5"/></svg>
      <svg width="11" height="11" viewBox="0 0 24 24" aria-label="Website"><g fill="none" stroke="#0f55a5" stroke-width="1.8"><circle cx="12" cy="12" r="10"/><ellipse cx="12" cy="12" rx="4.5" ry="10"/><path d="M2 12h20M4 6.5h16M4 17.5h16"/></g></svg>
    </div>
    <div class="lines lines--contact">
      <p>(+31 64-207 5184)</p>
      <p>info@thebrightlearner.example</p>
      <p>www.<span class="web-domain">thebrightlearner</span>.example</p>
    </div>
  </section>

  <section class="card card--back">
    <div class="brand">
      <span class="brand__dot"></span>
      <span class="brand__name">The Bright Learner</span>
    </div>
  </section>

</body>
</html>
```